New Business Card Design Project

Easy part first... I want the backside to be simple... jet black background with our logo in jet black/white/color. Feel free to play with tagline ideas under the logo if you want, I'm still toying around with it myself.

The front side... I need the logo on it, my photo headshot, and the following information:

Ray T. Dalworth
Top Producer
313-482-6157
dalworth.ray.t@mailnest.example
www.listlakeshorehomes.example
www.findlakeshorehomes.example

I'm looking for creativity with font, simple, but elegant, pairs well with the logo, good visibility of my photo, black background on the front as well, clearly see and identify information.
Updates

I would like the websites to have capitalization on the first letter of each word - www.ListLakeshoreHomes.example and www.FindLakeshoreHomes.example Also, I would like each of the capital letters to be slightly larger than the other font

Target Market(s)

We help people buy and sell homes from $50,000 to over a $1million.

Industry/Entity Type

Business

Requirements
Must have
• Must have information from above.
Nice to have
• Introducing a new color to be sharp against the black- possibly in the silver/nickel/platinum metallics? Feel free to crop the headshot down some if needed.
Should not have
• NO CHEESY GRAPHICS

```html
<!DOCTYPE html>
<html lang="en">
<head>
<meta charset="utf-8">
<title>Hearthway Real Estate – Business Card</title>
<link href="https://fonts.googleapis.com/css2?family=Fira+Sans:wght@400;600&display=swap" rel="stylesheet">
<style>
  :root {
    --backdrop: #7a5f40;
    --card-black: #050505;
    --band-blue: #22409a;
    --ink-white: #ffffff;
    --name-cream: #f3e7a6;
    --logo-gold: #b9a77a;
    --photo-light: #3a3b40;
    --photo-dark: #101012;
  }
  * { box-sizing: border-box; margin: 0; padding: 0; }
  html, body { width: 1200px; height: 1023px; overflow: hidden; }
  body {
    background: var(--backdrop);
    font-family: "Fira Sans", Arial, sans-serif;
    position: relative;
  }
  .card {
    position: absolute;
    width: 560px;
    height: 320px;
    background: var(--card-black);
    overflow: hidden;
    box-shadow: 0 10px 24px rgba(0,0,0,.45);
  }
  .card--front { left: 50px; top: 150px; }
  .card--back  { left: 600px; top: 540px; }

  .headshot {
    position: absolute;
    right: 0; top: 0;
    width: 300px; height: 210px;
    background: radial-gradient(ellipse at 40% 45%, var(--photo-light), var(--photo-dark) 75%);
  }
  .brand {
    display: flex; align-items: center; gap: 8px;
    color: var(--logo-gold);
    font-weight: 400;
    letter-spacing: 1px;
    text-transform: uppercase;
  }
  .brand__mark { width: 12px; height: 12px; background: var(--logo-gold); flex: none; }
  .card--front .brand { position: absolute; left: 26px; top: 150px; font-size: 13px; }

  .agent { position: absolute; left: 26px; top: 200px; }
  .agent__name { color: var(--name-cream); font-weight: 600; font-size: 22px; }
  .agent__title { color: var(--ink-white); font-size: 14px; margin-top: 2px; }

  .contact-band {
    position: absolute;
    right: 0; bottom: 0;
    width: 300px; height: 110px;
    background: var(--band-blue);
    padding: 12px 14px;
    display: flex; flex-direction: column; justify-content: center; gap: 4px;
  }
  .contact-line {
    display: flex; align-items: center; gap: 8px;
    color: var(--ink-white); font-size: 12.5px; white-space: nowrap;
  }
  .contact-line svg { width: 12px; height: 12px; flex: none; }

  .card--back .brand {
    position: absolute; left: 0; right: 0; top: 0; bottom: 0;
    justify-content: center; font-size: 24px; letter-spacing: 2px;
  }
  .card--back .brand__mark { width: 18px; height: 18px; }
</style>
</head>
<body>
  <section class="card card--front">
    <div class="headshot" role="img" aria-label="Headshot of the agent in a dark suit and blue tie"></div>
    <div class="brand"><span class="brand__mark"></span>Hearthway Real Estate</div>
    <div class="agent">
      <div class="agent__name">Ray T. Dalworth</div>
      <div class="agent__title">Top Producer</div>
    </div>
    <div class="contact-band">
      <div class="contact-line">
        <svg viewBox="0 0 12 12"><path d="M2.5 1l2 2.2-1.1 1.3a7 7 0 0 0 4.1 4.1l1.3-1.1 2.2 2-1.4 1.5C5.3 11 1 6.7 1 2.4z" fill="#fff"/></svg>
        313-482-6157
      </div>
      <div class="contact-line">
        <svg viewBox="0 0 12 12"><rect x="0.5" y="2" width="11" height="8" fill="#fff"/><path d="M0.5 2l5.5 4.5L11.5 2" stroke="#22409a" stroke-width="1.2" fill="none"/></svg>
        dalworth.ray.t@mailnest.example
      </div>
      <div class="contact-line">
        <svg viewBox="0 0 12 12"><circle cx="6" cy="6" r="5.5" fill="#fff"/><path d="M0.5 6h11M6 0.5v11M2.5 3h7M2.5 9h7" stroke="#22409a" stroke-width=".8"/></svg>
        www.listlakeshorehomes.example
      </div>
      <div class="contact-line">
        <svg viewBox="0 0 12 12"><circle cx="6" cy="6" r="5.5" fill="#fff"/><path d="M0.5 6h11M6 0.5v11M2.5 3h7M2.5 9h7" stroke="#22409a" stroke-width=".8"/></svg>
        www.findlakeshorehomes.example
      </div>
    </div>
  </section>

  <section class="card card--back">
    <div class="brand"><span class="brand__mark"></span>Hearthway Real Estate</div>
  </section>
</body>
</html>
```